Oil and Gas Exploration and Production company needs a business card design

We need a business card design using our logo and colors in the logo. We want a mainstream design.

```html
<!DOCTYPE html>
<html lang="en">
<head>
<meta charset="utf-8">
<title>Solara Oil &amp; Gas — Business Card, Front and Back</title>
<link rel="stylesheet" href="https://fonts.googleapis.com/css2?family=Cinzel:wght@600&family=Open+Sans:wght@400;600&display=swap">
<style>
  :root {
    --ink: #1b1b1b;
    --gold: #d4a72c;
    --paper: #fbfbf9;
    --back-light: #e4e4e2;
    --back-dark: #cfcfcc;
    --backdrop: #e6e4df;
    --rule: #6b6b6b;
  }
  html, body {
    margin: 0;
    width: 1200px;
    height: 1023px;
    overflow: hidden;
    background: var(--backdrop);
  }
  .card {
    position: absolute;
    left: 220px;
    width: 760px;
    height: 435px;
    border-radius: 26px;
    overflow: hidden;
    box-shadow: 0 8px 24px rgba(0,0,0,.16);
  }
  .card-front { top: 40px; background: var(--paper); }
  .card-back {
    top: 540px;
    background: linear-gradient(160deg, var(--back-light), var(--back-dark));
  }
  .card-band {
    position: absolute;
    inset: 0;
    width: 100%;
    height: 100%;
  }
  .brand {
    position: absolute;
    left: 53px;
    top: 128px;
    width: 280px;
    display: flex;
    align-items: center;
    gap: 14px;
  }
  .brand-dot {
    width: 35px;
    height: 35px;
    border-radius: 50%;
    background: var(--ink);
    flex: none;
  }
  .brand-name {
    font-family: "Cinzel", serif;
    font-weight: 600;
    font-size: 29px;
    line-height: 1.12;
    color: var(--ink);
    letter-spacing: 1px;
  }
  .divider {
    position: absolute;
    left: 357px;
    top: 53px;
    width: 2px;
    height: 243px;
    background: var(--rule);
  }
  .contact {
    position: absolute;
    left: 395px;
    top: 53px;
  }
  .person-name {
    font-family: "Cinzel", serif;
    font-weight: 600;
    font-size: 23px;
    color: var(--ink);
    margin: 0;
    letter-spacing: 1px;
  }
  .person-title {
    font-family: "Open Sans", sans-serif;
    font-size: 15px;
    color: var(--gold);
    margin: 2px 0 26px;
  }
  .contact-list {
    list-style: none;
    margin: 0;
    padding: 0;
    font-family: "Open Sans", sans-serif;
    font-size: 14.5px;
    color: var(--ink);
  }
  .contact-list li {
    display: flex;
    align-items: flex-start;
    gap: 11px;
    margin-bottom: 7px;
    line-height: 1.3;
  }
  .contact-icon {
    flex: none;
    width: 15px;
    height: 15px;
    margin-top: 2px;
    background: var(--gold);
    display: flex;
    align-items: center;
    justify-content: center;
  }
  .contact-icon svg { width: 11px; height: 11px; }
</style>
</head>
<body>
  <div class="card card-front">
    <svg class="card-band" viewBox="0 0 1000 572" preserveAspectRatio="none" aria-hidden="true">
      <path d="M0 572 L0 548 C 300 520, 700 470, 1000 345 L1000 572 Z" fill="var(--ink)"/>
      <path d="M0 572 L0 560 C 320 540, 720 495, 1000 375 L1000 572 Z" fill="var(--paper)"/>
      <path d="M60 572 C 360 555, 740 510, 1000 392 L1000 572 Z" fill="var(--gold)"/>
    </svg>

    <div class="brand">
      <span class="brand-dot"></span>
      <span class="brand-name">Solara<br>Oil &amp; Gas</span>
    </div>

    <div class="divider"></div>

    <div class="contact">
      <p class="person-name">Dale Whitford</p>
      <p class="person-title">CEO</p>
      <ul class="contact-list">
        <li>
          <span class="contact-icon"><svg viewBox="0 0 16 16"><path d="M4 1.5l2.5 3-1.5 1.5c.8 1.8 2.2 3.2 4 4l1.5-1.5 3 2.5-1.5 2.5C7 13.5 2.5 9 1.5 3z" fill="#fff"/></svg></span>
          +1 555-731-0066
        </li>
        <li>
          <span class="contact-icon"><svg viewBox="0 0 16 16"><rect x="3" y="2" width="10" height="4" fill="#fff"/><rect x="1.5" y="7" width="13" height="6" fill="#fff"/></svg></span>
          1 555-735-4764
        </li>
        <li>
          <span class="contact-icon"><svg viewBox="0 0 16 16"><rect x="1.5" y="3.5" width="13" height="9" fill="none" stroke="#fff" stroke-width="1.5"/><path d="M1.5 3.5L8 9l6.5-5.5" fill="none" stroke="#fff" stroke-width="1.5"/></svg></span>
          info@solaraoil.com
        </li>
        <li>
          <span class="contact-icon"><svg viewBox="0 0 16 16"><path d="M8 1.5a4.5 4.5 0 0 0-4.5 4.5C3.5 9.5 8 14.5 8 14.5s4.5-5 4.5-8.5A4.5 4.5 0 0 0 8 1.5z" fill="#fff"/><circle cx="8" cy="6" r="1.6" fill="var(--gold)"/></svg></span>
          <span>PO Box: , Midland, TX, USA,<br>Odessa, TX 79760-4120<br>Box : 4120</span>
        </li>
      </ul>
    </div>
  </div>

  <div class="card card-back" role="img" aria-label="Card back: light grey field with a faint repeating pattern of the company drop mark"></div>
</body>
</html>
```